We TEND toward Wedlock Event

I need a flyer to promote an Event we do that promotes Marriage and asks people to get involved in Ministry to Marriage. I need a graphic with the words: "We TEND toward Wedlock!"

Target Market(s)

Potential volunteers to get involve in the marriage ministry in a particular Catholic Parish.

Industry/Entity Type

Ministry

Logo Text

We TEND toward Wedlock!

Colors

Designer to choose colors to be used in the design.

Requirements
Must have
• Under the graphic should be the words: "An Event to Encourage and Support Marriages in our Parish"
• There could be a picture or pictures of married couples at different ages/stages.
• Other words include:
• "Please join us as we discuss the realities facing married couples today and what our response as a Parish can and should be."
• I also need a place to put name of Parish, date, time and location. This information will change for each event so the actual information will need to be left blank.
Nice to have
• Please make it eye-catching and something that would like to attend.
• WE hope the logo itself is fun and colorful.
• Would also like our non-profit logo along with the words "Conducted By..."(HearthWeaving USA) somewhere on flyer.

```html
<!DOCTYPE html>
<html lang="en">
<head>
<meta charset="utf-8">
<title>We TEND toward Wedlock! – Parish Event Flyer</title>
<link rel="stylesheet" href="https://fonts.googleapis.com/css2?family=EB+Garamond:wght@400;600&family=Great+Vibes&display=swap">
<style>
  :root {
    --page-bg: #e8e5e0;
    --teal-light: #1d6878;
    --teal-mid: #155261;
    --teal-deep: #0c3642;
    --frame-blue: #7db4c6;
    --ink-white: #ffffff;
    --ink-soft: #e6f0f2;
    --photo-warm: #d9c7b0;
    --photo-light: #f1ece4;
    --photo-shade: #8a7a6a;
  }
  * { margin: 0; padding: 0; box-sizing: border-box; }
  html, body { width: 1200px; height: 1200px; overflow: hidden; }
  body { background: var(--page-bg); position: relative; }

  .flyer {
    position: absolute; left: 185px; top: 30px;
    width: 830px; height: 1140px; overflow: hidden;
    background: radial-gradient(ellipse at 50% 40%, var(--teal-light) 0%, var(--teal-mid) 45%, var(--teal-deep) 100%);
    color: var(--ink-white);
    font-family: "EB Garamond", Georgia, serif;
  }

  .org { position: absolute; left: 290px; top: 22px; width: 270px; height: 100px; }
  .org-mark { position: absolute; left: 0; top: 8px; width: 56px; height: 56px; background: var(--ink-white); }
  .org-tagline { position: absolute; right: 0; top: 0; font-size: 13px; font-style: italic; font-weight: 600; }
  .org-name { position: absolute; left: 66px; top: 30px; font-size: 22px; font-weight: 600; white-space: nowrap; }
  .org-web { position: absolute; right: 0; top: 88px; font-size: 9px; }

  .headline-lead {
    position: absolute; left: 380px; top: 184px;
    font-size: 31px; letter-spacing: 0.5px; white-space: nowrap;
  }
  .headline-script {
    position: absolute; left: 0; width: 830px; top: 210px; text-align: center;
    font-family: "Great Vibes", cursive; font-size: 150px; line-height: 1;
  }

  .photo {
    position: absolute; border: 6px solid var(--frame-blue); border-radius: 34px;
    box-shadow: 0 10px 18px rgba(0,0,0,0.35);
  }
  .photo-left { left: 12px; top: 425px; width: 222px; height: 243px;
    background: linear-gradient(160deg, var(--photo-warm), var(--photo-light) 60%, #5a6fb0); }
  .photo-right { left: 596px; top: 425px; width: 222px; height: 243px;
    background: linear-gradient(200deg, #c9b98a, var(--photo-light) 55%, #6f86a8); }
  .photo-center { left: 172px; top: 382px; width: 496px; height: 329px; border-radius: 44px;
    background: linear-gradient(120deg, var(--photo-shade), var(--photo-warm) 40%, var(--photo-light) 70%, #d8d2c6); }

  .event-lead {
    position: absolute; left: 0; width: 830px; top: 746px; text-align: center;
    font-size: 26px; color: var(--ink-soft);
  }
  .event-script {
    position: absolute; left: 0; width: 830px; top: 776px; text-align: center;
    font-family: "Great Vibes", cursive; font-size: 58px; line-height: 1;
    text-shadow: 0.6px 0 0 var(--ink-white), -0.6px 0 0 var(--ink-white);
  }
  .invitation {
    position: absolute; left: 80px; width: 670px; top: 852px; text-align: center;
    font-size: 19px; line-height: 27px;
  }
  .details { position: absolute; left: 0; width: 830px; top: 926px; text-align: center; list-style: none; }
  .details li { font-size: 15px; letter-spacing: 0.4px; height: 50px; }
</style>
</head>
<body>
  <main class="flyer">
    <header class="org">
      <span class="org-mark"></span>
      <p class="org-tagline">"..Rebuild My Church!"</p>
      <p class="org-name">HearthWeaving USA</p>
      <p class="org-web">www.hearthweavingusa.org</p>
    </header>

    <h1>
      <span class="headline-lead">WE TEND TOWARD</span>
      <span class="headline-script">Wedlock!</span>
    </h1>

    <div class="photo photo-left" role="img" aria-label="Photo of a bride and groom standing on church steps"></div>
    <div class="photo photo-right" role="img" aria-label="Photo of a newlywed couple walking arm in arm"></div>
    <div class="photo photo-center" role="img" aria-label="Photo of a joyful bride and groom outdoors under her veil"></div>

    <p class="event-lead">An Event to Encourage and Support</p>
    <p class="event-script">Marriages in our Parish</p>

    <p class="invitation">Please join us as we discuss the realities facing married couples today and what our response as a Parish can and should be.</p>

    <ul class="details">
      <li>NAME OF PARISH</li>
      <li>DATE</li>
      <li>TIME &amp; LOCATION</li>
    </ul>
  </main>
</body>
</html>
```